Single Page website for Product Company

I need a website designed for my small startup company "Yard Leisure Crafts". We design and manufacture custom innovative indoor/outdoor entertainment furnishings e.g. outdoor TV enclosures, outdoor bars and outdoor kitchens. I'm looking for a single page site based on the the shopLite-SoloPage-ecommerce bootstrap page, attached.

I've also attached pictures of my products, these need to be photoshopped and placed in an outdoor patio area if possible.

Target Market(s)

Home owners

Industry/Entity Type

It Company

Coding

Coded - Design and coding required

Number of Pages Required

1 page

Requirements
Must have
• Must be single page site built with attached bootstrap template and adjust to screen size e.g. ipad, mobile phone and computer
Nice to have
• Integration with vendora

```html
<!DOCTYPE html>
<html lang="en">
<head>
<meta charset="utf-8">
<title>Yard Leisure Crafts</title>
<link rel="stylesheet" href="https://fonts.googleapis.com/css2?family=Jost:wght@300;400;500;600&display=swap">
<style>
:root{
  --orange:#f7941d;
  --blue:#3fa2f0;
  --green:#56c40c;
  --ink:#2b2b2b;
  --muted:#6f6f6f;
  --line:#d9d9d9;
  --soft:#f0f0f0;
  --white:#ffffff;
  --footer:#1d1d1d;
}
*{box-sizing:border-box;margin:0;padding:0}
html,body{width:1200px;height:3644px;overflow:hidden}
body{position:relative;font-family:'Jost',sans-serif;color:var(--ink);background:var(--white)}
.abs{position:absolute}
.photo{position:absolute}

/* hero */
.hero{position:absolute;left:0;top:0;width:1200px;height:505px;
  background:linear-gradient(180deg,#1b2230 0%,#3a3026 45%,#5a4634 70%,#2a2a2c 100%)}
.hero-shade{position:absolute;inset:0;background:linear-gradient(180deg,rgba(0,0,0,.35),rgba(0,0,0,.15) 50%,rgba(0,0,0,.3))}
.brand{position:absolute;left:214px;top:36px;display:flex;align-items:center;gap:10px;color:var(--white);font-size:22px;font-weight:500}
.brand-mark{width:26px;height:26px;border:2px solid var(--white)}
.nav{position:absolute;top:42px;left:583px;display:flex;gap:0;font-size:14px;color:var(--white);font-weight:500}
.nav a{position:absolute;white-space:nowrap;color:var(--white);text-decoration:none}
.nav a.active{color:var(--orange)}
.nav a.active::after{content:"";position:absolute;left:0;right:0;top:-42px;height:3px;background:var(--orange)}
.social{position:absolute;display:flex;gap:8px}
.social span{width:22px;height:22px;border-radius:50%;border:1.5px solid var(--white)}
.social span.on{background:var(--blue);border-color:var(--blue)}
.hero-title{position:absolute;left:0;width:1200px;top:236px;text-align:center;color:var(--white);font-size:25px;font-weight:400;line-height:31px}
.hero-title em{font-style:normal;color:var(--orange)}
.btn{position:absolute;display:flex;align-items:center;justify-content:center;color:var(--white);font-size:13px;font-weight:500}
.btn-blue{background:var(--blue)}
.btn-orange{background:var(--orange)}
.arrow{position:absolute;width:28px;height:28px;border-radius:50%}
.arrow-line{border:1.5px solid var(--white)}
.arrow-fill{background:var(--orange)}

/* products */
.section-title{position:absolute;left:0;width:1200px;text-align:center;font-size:20px;font-weight:500;color:var(--ink)}
.section-title::after{content:"";display:block;width:36px;height:2px;background:var(--blue);margin:12px auto 0}
.product-img{position:absolute;width:369px;height:321px}
.product-name{position:absolute;font-size:16px;font-weight:500}
.product-desc{position:absolute;width:240px;font-size:12px;line-height:15px;color:var(--muted)}
.price{position:absolute;font-size:22px;color:var(--orange);font-weight:400}
.dots{position:absolute;display:flex;gap:8px}
.dots span{width:18px;height:18px;border-radius:50%;border:1.5px solid var(--orange)}
.dots span.on{background:var(--orange)}

/* shipping band */
.ship{position:absolute;left:0;top:1691px;width:1200px;height:97px;background:linear-gradient(90deg,#3d9ef0,#4fb0f5)}
.ship-text{position:absolute;left:340px;top:34px;color:var(--white);font-size:20px;font-weight:500}

/* about */
.about-left{position:absolute;left:0;top:1788px;width:600px;height:419px;background:var(--soft)}
.about-title{position:absolute;left:209px;top:1846px;font-size:20px;font-weight:500}
.about-title::after{content:"";display:block;width:36px;height:2px;background:var(--blue);margin-top:10px}
.about-text{position:absolute;left:209px;width:390px;font-size:12.5px;line-height:18px;color:var(--muted)}

/* order form */
.order-table{position:absolute;left:209px;top:2322px;width:785px;border-collapse:collapse;font-size:12px}
.order-table th{text-align:left;font-weight:600;height:24px;border-bottom:1px solid var(--line)}
.order-table td{height:31px;color:var(--muted);border-bottom:1px solid var(--line)}
.order-table .num{text-align:right}
.qty{display:inline-block;width:42px;height:20px;border:1px solid var(--line);font-size:11px;padding:2px 6px}
.form-head{position:absolute;font-size:14px;font-weight:500;text-align:center}
.field{position:absolute;height:30px;border:1px solid var(--line);font-size:11px;color:#9a9a9a;padding:8px 8px}
.sum-row{position:absolute;left:612px;width:379px;display:flex;justify-content:space-between;font-size:11px;color:var(--muted);border-bottom:1px solid var(--line);padding-bottom:6px}

/* features */
.feature{position:absolute;top:2870px;width:400px;height:175px;color:var(--white);text-align:center}
.feature svg{position:absolute;left:170px;top:38px}
.feature p{position:absolute;left:0;width:100%;top:118px;font-size:16px;font-weight:500}

/* footer */
.footer-left{position:absolute;left:0;top:3246px;width:600px;height:398px;background:linear-gradient(160deg,#262626,#141414)}
.footer-right{position:absolute;left:600px;top:3246px;width:600px;height:398px;background:linear-gradient(135deg,#3e3e3e,#2b2b2b 60%,#4a3e36)}
.foot-h{position:absolute;font-size:20px;font-weight:500;color:var(--white)}
.foot-t{position:absolute;font-size:12px;color:#e6e6e6;line-height:17px}
.foot-label{position:absolute;left:644px;font-size:12px;color:#e6e6e6}
.foot-line{position:absolute;left:644px;width:347px;height:1px;background:#bdbdbd}
</style>
</head>
<body>

<!-- hero -->
<header class="hero" role="img" aria-label="Evening outdoor patio with a stone fireplace, mounted TV, pool and bistro seating">
  <div class="hero-shade"></div>
</header>
<div class="brand"><span class="brand-mark"></span>Yard Leisure Crafts</div>
<nav class="nav">
  <a class="active" style="left:0">Product</a>
  <a style="left:87px">About</a>
  <a style="left:163px">Order</a>
  <a style="left:241px">Contact</a>
</nav>
<div class="social" style="left:907px;top:40px"><span class="on"></span><span></span><span></span></div>
<h1 class="hero-title">We design and manufacture custom innovative<br><em>indoor/outdoor</em> entertainment <em>furnishings</em></h1>
<a class="btn btn-blue" style="left:540px;top:316px;width:123px;height:29px">Shop Now</a>
<svg class="arrow arrow-line" style="left:127px;top:278px" viewBox="0 0 28 28"><path d="M16 9l-5 5 5 5" fill="none" stroke="#fff" stroke-width="1.8"/></svg>
<svg class="arrow arrow-fill" style="left:1043px;top:278px" viewBox="0 0 28 28"><path d="M12 9l5 5-5 5" fill="none" stroke="#fff" stroke-width="1.8"/></svg>

<!-- products -->
<h2 class="section-title" style="top:545px">Our Products</h2>

<div class="product-img" style="left:275px;top:617px;background:linear-gradient(160deg,#6b8a5a,#8a6e54 50%,#c9c3b6)" role="img" aria-label="Stone outdoor TV enclosure on a garden patio"></div>
<h3 class="product-name" style="left:685px;top:662px">Outdoor TV enclosures</h3>
<p class="product-desc" style="left:685px;top:690px">Lorem Ipsum is simply dummy text of the printing and typesetting industry. Lorem Ipsum has been the industry's standard dummy text ever since the 1500s.</p>
<p class="price" style="left:685px;top:770px">$500</p>
<a class="btn btn-orange" style="left:685px;top:817px;width:110px;height:27px">Shop Now</a>
<div class="dots" style="left:689px;top:868px"><span></span><span class="on"></span></div>

<div class="product-img" style="left:554px;top:972px;background:linear-gradient(150deg,#2a2a2e,#5a6270 45%,#3f7fb2 70%,#1f1f22)" role="img" aria-label="Outdoor bar with a colourful mosaic counter and bar stools"></div>
<h3 class="product-name" style="left:275px;top:1018px">Outdoor Bars</h3>
<p class="product-desc" style="left:275px;top:1046px">Lorem Ipsum is simply dummy text of the printing and typesetting industry. Lorem Ipsum has been the industry's standard dummy text ever since the 1500s.</p>
<p class="price" style="left:275px;top:1125px">$500</p>
<a class="btn btn-blue" style="left:275px;top:1171px;width:110px;height:27px">Shop Now</a>
<div class="dots" style="left:279px;top:1222px"><span></span><span></span></div>

<div class="product-img" style="left:275px;top:1327px;background:linear-gradient(170deg,#3c3c3a,#7d8a6a 35%,#a88a6a 65%,#6b5846)" role="img" aria-label="Outdoor kitchen with stone counter, grill and range hood"></div>
<h3 class="product-name" style="left:685px;top:1373px">Outdoor Kitchens</h3>
<p class="product-desc" style="left:685px;top:1401px">Lorem Ipsum is simply dummy text of the printing and typesetting industry. Lorem Ipsum has been the industry's standard dummy text ever since the 1500s....</p>
<p class="price" style="left:685px;top:1480px">$1000</p>
<a class="btn btn-blue" style="left:685px;top:1526px;width:110px;height:27px">Shop Now</a>
<div class="dots" style="left:689px;top:1578px"><span></span><span></span></div>

<!-- shipping band -->
<section class="ship">
  <svg class="abs" style="left:292px;top:28px" width="40" height="40" viewBox="0 0 40 40"><path d="M30 8c-8 0-14 6-17 13l6 6c7-3 13-9 13-17zM13 21l-5 1 3-6 6-1M19 27l-1 5 6-3 1-6M12 28l-4 4" fill="none" stroke="#fff" stroke-width="1.8" stroke-linejoin="round"/><circle cx="24" cy="16" r="2.5" fill="none" stroke="#fff" stroke-width="1.6"/></svg>
  <p class="ship-text">Free international shipping only 2 days 21:19:10</p>
  <a class="btn btn-orange" style="left:880px;top:37px;width:109px;height:27px">Order Now</a>
</section>

<!-- about -->
<div class="about-left"></div>
<div class="photo" style="left:600px;top:1788px;width:600px;height:419px;background:linear-gradient(90deg,#e9e9e7,#b7b4ae 40%,#4d4a48 75%,#6b6870)" role="img" aria-label="Living room with a white wall-mounted TV unit"></div>
<h2 class="about-title">About Us</h2>
<p class="about-text" style="top:1908px">Lorem Ipsum is simply dummy text of the printing and typesetting industry. Lorem Ipsum has been the industry's standard dummy text ever since the 1500s, when an unknown printer took a galley of type and scrambled it to make a type specimen book. It has survived not only five centuries, but also the leap into electronic.</p>
<p class="about-text" style="top:2032px">typesetting, remaining essentially unchanged. It was popularised in the 1960s with the release of Letraset sheets containing Lorem Ipsum passages, and more recently with desktop publishing software like Aldus PageMaker including versions of Lorem Ipsum.</p>

<!-- order form -->
<h2 class="section-title" style="top:2246px">Order Form</h2>
<table class="order-table">
  <tr><th style="width:245px">Product</th><th style="width:221px">Unit Cost</th><th>Quantity</th><th class="num">Total</th></tr>
  <tr><td>Bed</td><td>$500</td><td><span class="qty">0 ▾</span></td><td class="num">$0</td></tr>
  <tr><td>Nightstand</td><td>$200</td><td><span class="qty">0 ▾</span></td><td class="num">$0</td></tr>
  <tr><td>Hammock</td><td>$700</td><td><span class="qty">0 ▾</span></td><td class="num">$0</td></tr>
</table>

<p class="form-head" style="left:209px;width:379px;top:2481px">Payment Method</p>
<div class="field" style="left:209px;top:2517px;width:187px">Card number</div>
<div class="field" style="left:408px;top:2517px;width:180px">Code</div>
<div class="field" style="left:209px;top:2556px;width:187px">January<span style="float:right">▾</span></div>
<div class="field" style="left:408px;top:2556px;width:180px">2014<span style="float:right">▾</span></div>
<p class="form-head" style="left:209px;width:379px;top:2600px">Information</p>
<div class="field" style="left:209px;top:2636px;width:187px">First Name</div>
<div class="field" style="left:408px;top:2636px;width:180px">Last Name</div>
<div class="field" style="left:209px;top:2675px;width:379px">Your Email</div>
<p class="form-head" style="left:209px;width:379px;top:2721px">If you have Coupon Code</p>
<div class="field" style="left:209px;top:2756px;width:301px">Coupon Code</div>
<a class="btn btn-blue" style="left:510px;top:2756px;width:78px;height:30px;font-size:11px">Check !</a>

<p class="form-head" style="left:612px;width:379px;top:2481px">Delivery Address</p>
<div class="field" style="left:612px;top:2515px;width:379px">Street Address</div>
<div class="field" style="left:612px;top:2555px;width:379px">City</div>
<div class="field" style="left:612px;top:2595px;width:379px">Country</div>
<div class="field" style="left:612px;top:2634px;width:379px">Post Code</div>
<p class="form-head" style="left:612px;width:379px;top:2682px">Order Summary</p>
<div class="sum-row" style="top:2728px"><span>Shipping cost:</span><span>Free</span></div>
<div class="sum-row" style="top:2760px"><span>Total:</span><span>$0.00</span></div>
<a class="btn btn-blue" style="left:612px;top:2797px;width:379px;height:29px;font-size:11px">Order Product</a>

<!-- features -->
<section class="feature" style="left:0;background:var(--orange)">
  <svg width="60" height="60" viewBox="0 0 60 60"><circle cx="30" cy="22" r="14" fill="none" stroke="#fff" stroke-width="3"/><path d="M23 22l5 5 9-9" fill="none" stroke="#fff" stroke-width="3"/><path d="M21 34l-6 18 8-4 4 7 3-14M39 34l6 18-8-4-4 7-3-14" fill="none" stroke="#fff" stroke-width="2.5" stroke-linejoin="round"/></svg>
  <p>Quality Guaranteed</p>
</section>
<section class="feature" style="left:400px;background:var(--blue)">
  <svg width="60" height="60" viewBox="0 0 60 60"><rect x="14" y="14" width="28" height="24" fill="#fff"/><path d="M42 22h9l6 8v8H42z" fill="#fff"/><circle cx="22" cy="42" r="5" fill="#fff" stroke="#3fa2f0" stroke-width="2"/><circle cx="48" cy="42" r="5" fill="#fff" stroke="#3fa2f0" stroke-width="2"/><path d="M2 20h9M0 27h11M4 34h7" stroke="#fff" stroke-width="2.5"/></svg>
  <p>Home Delivery</p>
</section>
<section class="feature" style="left:800px;background:var(--green)">
  <svg width="60" height="60" viewBox="0 0 60 60"><rect x="18" y="10" width="38" height="26" rx="3" fill="none" stroke="#fff" stroke-width="3"/><path d="M18 18h38" stroke="#fff" stroke-width="4"/><rect x="6" y="32" width="24" height="20" rx="2" fill="#fff"/><path d="M11 32v-6a7 7 0 0114 0v6" fill="none" stroke="#fff" stroke-width="3"/></svg>
  <p>Secure Payment</p>
</section>

<!-- newsletter -->
<h2 class="section-title" style="top:3084px">Stay in touch</h2>
<div class="field" style="left:389px;top:3159px;width:328px;height:29px">Enter your email</div>
<a class="btn btn-blue" style="left:717px;top:3159px;width:92px;height:29px;font-size:12px">Subscribe</a>

<!-- footer -->
<footer>
  <div class="footer-left"></div>
  <div class="footer-right" role="img" aria-label="Blurred close-up of hands typing on a keyboard"></div>
  <svg class="abs" style="left:586px;top:3232px" width="28" height="28" viewBox="0 0 28 28"><circle cx="14" cy="14" r="14" fill="#f7941d"/><path d="M9 16l5-5 5 5" fill="none" stroke="#fff" stroke-width="2"/></svg>

  <h3 class="foot-h" style="left:209px;top:3322px">Contact Us</h3>
  <p class="foot-t" style="left:209px;top:3362px">Call Us:</p>
  <p class="foot-t" style="left:209px;top:3378px;font-size:17px;color:#fff">+1 (650) 555-0198</p>
  <p class="foot-t" style="left:209px;top:3402px">hello@yardleisurecrafts.example</p>
  <p class="foot-t" style="left:209px;top:3422px">Location:</p>
  <p class="foot-t" style="left:209px;top:3439px">17 Garden Lane 45,City<br>State 30917</p>
  <div class="social" style="left:209px;top:3500px"><span style="background:var(--orange);border-color:var(--orange)"></span><span></span><span></span></div>
  <p class="foot-t" style="left:209px;top:3549px">© Copyright 2017 Yard Leisure Crafts.</p>

  <h3 class="foot-h" style="left:644px;top:3298px">Send us Message</h3>
  <p class="foot-label" style="top:3342px">Your Name</p>
  <div class="foot-line" style="top:3368px"></div>
  <p class="foot-label" style="top:3394px">Enter Email</p>
  <div class="foot-line" style="top:3417px"></div>
  <p class="foot-label" style="top:3443px">Your Message</p>
  <div class="foot-line" style="top:3528px"></div>
  <a class="btn btn-blue" style="left:644px;top:3560px;width:95px;height:27px;font-size:12px">Send ➜</a>
</footer>

</body>
</html>
```